Real estate business card

I need a business card for my real estate company. I help clients buy and sell properties. I would like to keep the design very simple and professional. I would like the design to convey professionalism, safety and trust. I prefer no graphics but a simple logo design would be nice if that is part of what you do.
Updates

Please keep the designs simple. No high-rise buildings please. 

Reason: My design has not been finalized.

Target Market(s)

Age group 30-60 mostly affluent

Industry/Entity Type

Real Estate

Contact Information for Business Card

Velmont Realtors
Howard Prisk, Broker
4153 Marlow Ave. #226, La Crescenta, CA 91207

Requirements
Nice to have
• Logo can be combination of my initials HP or just Z or a simple geometric shape? Please see "Desig Ideas" attachment. No pics of houses or shaking hands, dollar bills, $, %, etc...
Please use fonts similar to Helvetica for a clean, modern look (think Northern European design, simple, clean yet bold)

Also use font colors such as blue, grey in different shades. Use pastel colors if better.

```html
<!DOCTYPE html>
<html lang="en">
<head>
<meta charset="utf-8">
<title>Howard Prisk – Broker</title>
<link rel="stylesheet" href="https://fonts.googleapis.com/css2?family=Saira+Condensed:wght@300;400;600&display=swap">
<style>
  :root {
    --page: #ffffff;
    --card: #272525;
    --card-edge: #5a5858;
    --ink: #f3f3f3;
    --divider: #8a8888;
    --mark-blue: #3550b0;
  }
  html, body {
    margin: 0;
    padding: 0;
    width: 1200px;
    height: 678px;
    overflow: hidden;
    background: var(--page);
  }
  .card {
    position: relative;
    box-sizing: border-box;
    width: 1200px;
    height: 678px;
    background: var(--card);
    border: 2px solid var(--card-edge);
    border-radius: 14px 40px 60px 14px;
    color: var(--ink);
    font-family: "Saira Condensed", "Arial Narrow", sans-serif;
  }
  .identity {
    position: absolute;
    left: 70px;
    top: 82px;
    width: 531px;
  }
  .name {
    margin: 0;
    font-weight: 300;
    font-size: 88px;
    line-height: 1;
    letter-spacing: 2px;
    white-space: nowrap;
    padding-bottom: 8px;
    border-bottom: 4px solid var(--ink);
  }
  .details {
    position: absolute;
    right: 603px;
    top: 228px;
    text-align: right;
  }
  .role {
    margin: 0;
    font-weight: 400;
    font-size: 58px;
    line-height: 1;
    letter-spacing: 17px;
    margin-right: -17px;
  }
  .licence {
    margin: 4px 0 0;
    font-weight: 600;
    font-size: 30px;
    letter-spacing: 2px;
    line-height: 1.1;
  }
  .address {
    margin: 48px 0 0;
    font-style: normal;
    font-weight: 400;
    font-size: 31px;
    line-height: 42px;
    letter-spacing: 1px;
  }
  .contact {
    margin: 40px 0 0;
    font-weight: 400;
    font-size: 31px;
    line-height: 42px;
    letter-spacing: 1px;
  }
  .divider {
    position: absolute;
    left: 659px;
    top: 22px;
    width: 4px;
    height: 628px;
    background: var(--divider);
  }
  .monogram {
    position: absolute;
    left: 760px;
    top: 96px;
    width: 360px;
    height: 512px;
    display: flex;
    align-items: center;
    justify-content: center;
    font-family: "Saira Condensed", "Arial Narrow", sans-serif;
    font-weight: 600;
    font-size: 330px;
    line-height: 1;
    color: var(--mark-blue);
    letter-spacing: -4px;
  }
</style>
</head>
<body>
  <main class="card">
    <section class="identity">
      <h1 class="name">Howard Prisk</h1>
    </section>
    <section class="details">
      <p class="role">Broker</p>
      <p class="licence">CA BRE 01384517</p>
      <address class="address">4153 Marlow Ave<br>#226, La Crescenta, CA 91207</address>
      <p class="contact">Contact (818) 555-0172<br>Email: howardprisk@velmontmail.com</p>
    </section>
    <div class="divider"></div>
    <div class="monogram">HP</div>
  </main>
</body>
</html>
```